Business Card Design

We are a General Practice - Family medicine
We also have Allied Health professionals working within our team

Industry/Entity Type

Business

Contact Information for Business Card

Front of the card to display:

BRAMBLEWICK MEDICAL
PHONE 6348 2917

5/41 Fennimore Parade
Launceston Tasmania 7284

Back of the card to display:

My Appointments
Date:
Time:
With:

Please remember to phone us on 6348 2917 to cancel your appointment if you can't keep it.
A fee applied to missed appointments

```html
<!DOCTYPE html>
<html lang="en">
<head>
<meta charset="utf-8">
<title>Bramblewick Medical – Business Cards</title>
<link rel="stylesheet" href="https://fonts.googleapis.com/css2?family=Open+Sans:wght@400;600&family=Cinzel:wght@400&display=swap">
<style>
  :root {
    --page-bg: #e4e4e4;
    --card-bg: #ffffff;
    --brand-blue: #2f8fd0;
    --brand-blue-deep: #1f78bf;
    --brand-green: #6cbb3c;
    --ink: #4a4a4a;
    --rule: #9a9a9a;
    --white: #ffffff;
  }
  * { box-sizing: border-box; margin: 0; padding: 0; }
  html, body {
    width: 1200px; height: 852px; overflow: hidden;
    background: var(--page-bg);
    font-family: "Open Sans", Arial, sans-serif;
  }
  .sheet {
    width: 1200px; height: 852px;
    display: flex; align-items: center; justify-content: center; gap: 40px;
  }
  .card {
    position: relative;
    width: 540px; height: 310px;
    border-radius: 22px;
    background: var(--card-bg);
    overflow: hidden;
    box-shadow: 0 6px 16px rgba(0,0,0,0.18);
  }
  .brand {
    position: absolute;
    display: flex; align-items: center; gap: 14px;
  }
  .brand-mark {
    width: 40px; height: 40px; border-radius: 50%;
    background: var(--brand-green);
  }
  .brand-name {
    font-family: "Open Sans", Arial, sans-serif;
    font-weight: 400;
    font-size: 34px;
    color: var(--brand-blue);
    letter-spacing: -0.5px;
  }

  /* Appointment card */
  .appointment .brand { left: 36px; top: 30px; }
  .appointment-title {
    position: absolute; left: 0; right: 0; top: 98px;
    text-align: center;
    font-family: "Cinzel", Georgia, serif;
    font-size: 19px; letter-spacing: 1.5px;
    color: var(--ink);
  }
  .entry-row {
    position: absolute; left: 36px; right: 36px;
    display: flex; align-items: flex-end; gap: 8px;
    font-size: 14px; color: var(--ink);
  }
  .entry-row .label { white-space: nowrap; }
  .entry-row .field { flex: 1; border-bottom: 1px solid var(--rule); height: 16px; }
  .entry-row.with { top: 144px; }
  .entry-row.date-time { top: 184px; }
  .entry-row.date-time .field.date { flex: 1.4; margin-right: 14px; }
  .reminder-band {
    position: absolute; left: 0; right: 0; bottom: 0; height: 74px;
    background: linear-gradient(180deg, var(--brand-blue), var(--brand-blue-deep));
    color: var(--white);
    display: flex; flex-direction: column; justify-content: center; align-items: center;
    text-align: center; font-size: 12.5px; line-height: 1.55;
  }
  .reminder-band .fee { font-weight: 600; font-size: 11.5px; letter-spacing: 0.4px; }

  /* Contact card */
  .contact-wave { position: absolute; inset: 0; }
  .contact .brand { left: 40px; top: 52px; }
  .contact-details {
    position: absolute; left: 150px; right: 30px; top: 192px;
    color: var(--white); text-align: center;
  }
  .phone {
    display: flex; align-items: center; justify-content: center; gap: 12px;
    font-size: 22px; margin-bottom: 22px;
  }
  .phone svg { width: 22px; height: 22px; }
  .address { font-size: 14px; letter-spacing: 0.2px; }
</style>
</head>
<body>
<main class="sheet">

  <section class="card appointment" aria-label="Appointment card">
    <div class="brand">
      <span class="brand-mark"></span>
      <span class="brand-name">Bramblewick Medical</span>
    </div>
    <h2 class="appointment-title">MY APPOINTMENTS</h2>
    <div class="entry-row with">
      <span class="label">With:</span><span class="field"></span>
    </div>
    <div class="entry-row date-time">
      <span class="label">Date:</span><span class="field date"></span>
      <span class="label">Time:</span><span class="field"></span>
    </div>
    <div class="reminder-band">
      <p>Please remember to phone us on 6348 2917 to cancel your appointment if you can't keep it.</p>
      <p class="fee">A FEE APPLIED TO MISSED APPOINTMENTS</p>
    </div>
  </section>

  <section class="card contact" aria-label="Contact card">
    <svg class="contact-wave" viewBox="0 0 540 310" preserveAspectRatio="none" aria-hidden="true">
      <defs>
        <linearGradient id="waveBlue" x1="0" y1="0" x2="0" y2="1">
          <stop offset="0" stop-color="#3a9ad6"/>
          <stop offset="1" stop-color="#1f78bf"/>
        </linearGradient>
      </defs>
      <path d="M0 248 C150 200 330 150 540 120 L540 310 L0 310 Z" fill="url(#waveBlue)"/>
      <path d="M0 240 C150 192 330 142 540 112" fill="none" stroke="#6cbb3c" stroke-width="4"/>
    </svg>
    <div class="brand">
      <span class="brand-mark"></span>
      <span class="brand-name">Bramblewick Medical</span>
    </div>
    <div class="contact-details">
      <p class="phone">
        <svg viewBox="0 0 24 24" aria-label="Phone" role="img"><path fill="#ffffff" d="M4 9c0-3 3-5 8-5s8 2 8 5l-1 2-3-1V8c-2-1-6-1-8 0v2l-3 1zM7 12h10l2 7H5z"/></svg>
        <span>6348 2917</span>
      </p>
      <p class="address">5/41 Fennimore Parade Launceston Tasmania 7284</p>
    </div>
  </section>

</main>
</body>
</html>
```